Velbrook Leaf is a bridge for the people who drink tea to connect with the people who make the tea and the environment in which it is grown.

As a start-up, Velbrook Leaf needs to establish a fluently persuasive brand image that articulates its unique mission to the up-market tea drinker.

Our passion for high quality tea and our respect for people are boundless. But our budget is shoe-string. Still, we will allocate a disproportionate amount to evolving a brand; including logo, labeling, and packaging, and hope this initial effort will lead to a long-term relationship with a designer. The Velbrook label, as a component of the brand, must deny the commodity image of tea by broadcasting the uniquely flavorful, healthful, and relaxing experience of drinking tea.

The logo is an image of a liquor pouring from above into a stylized outline of a cup and gracefully folding over on itself within the cup. The image is an echo of video clips that will be featured on the Product page of the ecommerce site. Our initial thought is for the liquor and cup to be white on a rich blue background. But you may have a better idea.

The label must fit a seamless tin canister 4" in diameter; 2" high with a "window" in the lid. There are really three distinct parts to the label: a) wrap-around for the body of the tin; b) a distinct piece to be applied underneath the tin; and c) security strip (s) that connect the lid and the bottom of the tin. The wrap-around must include the following components: the logo, the brand name 'Velbrook Leaf', the name of the specific tea and space for the following characteristics of the tea: Tea / Garden Name, Harvest Date, Tasting Notes, Weight, Location, and Caffeine content. The piece to be affixed underneath the tin should accommodate Ingredients, Brewing Instructions, and contact details for Velbrook Leaf. The security strip(s) should be an integral part of the overall visual.

The color scheme should be expandable, i.e.; different colors for different teas.
We are thinking about rich and bold colors. But am eager to see what inspires you!

A very rough proto-type is captured in the attached files.

Target Market(s)

Ages 25 to 45 in densely populated areas of the U.S. and Canada will an above average house-hold income and an interest in what they eat / drink.

Industry/Entity Type

Environment

Requirements
Must have
• 1. Three separate pieces: 1) wrap around for the body of the tin; 2) piece to be affixed to the bottom of the body of the tin; 3) security strip (s). A word about strips: am unsure about one vs two because, two will add to overhead and processing while one will block the view of the contents. Maybe you know how to resolve.
2. clean, crisp lines
3. uncluttered
Nice to have
• 1. a color scheme to accommodate up to 30 different teas. Do not fall into the trap of incorporating the color green on the label for a 'green tea' and yellow for a lemon flavored tea. That approach is limited and has been overdone.
2. a color scheme that, as it expands to accommodate 30 teas, also is anchored by a brand color set. In other words, all labels include a recognizable color set.
3. express the level of caffeine via a gauge or metric
Should not have
• photo images,

```html
<!DOCTYPE html>
<html lang="en">
<head>
<meta charset="utf-8">
<title>Velbrook Leaf – Tin Label Wrap</title>
<link rel="stylesheet" href="https://fonts.googleapis.com/css2?family=Advent+Pro:wght@400;500&family=Roboto+Condensed:wght@400&display=swap">
<style>
  :root {
    --brand-orange: #f28a35;
    --paper: #ffffff;
    --roast: #5b3a2b;
    --tagline: #8a5637;
    --rule: #ffffff;
  }
  html, body {
    margin: 0;
    padding: 0;
    overflow: hidden;
    background: var(--paper);
  }
  .label {
    position: relative;
    width: 930px;
    height: 1200px;
    background: var(--paper);
    overflow: hidden;
  }
  .band {
    position: absolute;
    top: 0;
    height: 1200px;
    background: var(--brand-orange);
  }
  .band--brand { left: 0; width: 304px; }
  .band--caffeine { left: 630px; width: 300px; }

  .brand-mark {
    position: absolute;
    left: 30px;
    top: 600px;
    width: 244px;
    display: flex;
    align-items: center;
    justify-content: center;
    gap: 14px;
    color: var(--paper);
    font-family: "Advent Pro", sans-serif;
    font-weight: 500;
    font-size: 44px;
    line-height: 1.05;
  }
  .brand-mark__dot {
    flex: none;
    width: 20px;
    height: 20px;
    border-radius: 50%;
    background: var(--paper);
  }
  .brand-mark__name { margin: 0; }

  .band__rule {
    position: absolute;
    left: 0;
    top: 816px;
    width: 304px;
    height: 5px;
    background: var(--rule);
  }

  .tagline {
    position: absolute;
    left: 0;
    top: 890px;
    width: 304px;
    margin: 0;
    text-align: center;
    color: var(--tagline);
    font-family: "Advent Pro", sans-serif;
    font-weight: 400;
    font-size: 50px;
    line-height: 84px;
  }

  .caffeine-gauge {
    position: absolute;
    left: 728px;
    top: 484px;
    width: 104px;
    display: flex;
    flex-direction: column;
    gap: 10px;
    margin: 0;
    padding: 0;
    list-style: none;
  }
  .caffeine-gauge__cell {
    height: 107px;
    display: flex;
    align-items: center;
    justify-content: center;
    background: var(--paper);
    color: var(--roast);
    font-family: "Roboto Condensed", sans-serif;
    font-size: 62px;
  }
  .caffeine-gauge__cell--filled {
    background: var(--roast);
    color: var(--paper);
  }
  .caffeine-gauge__letter {
    display: inline-block;
    transform: rotate(-90deg);
    line-height: 1;
  }
</style>
</head>
<body>
  <main class="label">
    <section class="band band--brand">
      <div class="brand-mark">
        <span class="brand-mark__dot"></span>
        <p class="brand-mark__name">Velbrook<br>Leaf</p>
      </div>
      <div class="band__rule"></div>
      <p class="tagline">Your<br>artisanal<br>connection</p>
    </section>

    <section class="band band--caffeine" aria-label="Caffeine level">
    </section>
    <ol class="caffeine-gauge" aria-label="Caffeine: medium">
      <li class="caffeine-gauge__cell"><span class="caffeine-gauge__letter">E</span></li>
      <li class="caffeine-gauge__cell"><span class="caffeine-gauge__letter">N</span></li>
      <li class="caffeine-gauge__cell"><span class="caffeine-gauge__letter">EI</span></li>
      <li class="caffeine-gauge__cell caffeine-gauge__cell--filled"><span class="caffeine-gauge__letter">FF</span></li>
      <li class="caffeine-gauge__cell caffeine-gauge__cell--filled"><span class="caffeine-gauge__letter">A</span></li>
      <li class="caffeine-gauge__cell caffeine-gauge__cell--filled"><span class="caffeine-gauge__letter">C</span></li>
    </ol>
  </main>
</body>
</html>
```